Railroad Association needs One-Page Infographic

Please see attachment for text and graphic. email with questions please. This piece will be handed out to legislators and state officials.

Target Market(s)

state legislature. state officials

Font styles to use
Serif

Colors
ec1f27

Requirements
Must have
• The graphic needs to be done right. Please email me with any questions.

```html
<!DOCTYPE html>
<html lang="en">
<head>
<meta charset="utf-8">
<title>Crossing Railroad Right of Way – What Is the Process?</title>
<link href="https://fonts.googleapis.com/css2?family=Roboto+Condensed:wght@300;400;700&display=swap" rel="stylesheet">
<style>
  :root {
    --ink: #000000;
    --paper: #ffffff;
    --stage: #e9eaec;
    --amber: #f8b71d;
    --gold: #d59b28;
    --gold-box: #d4a02f;
    --sign-fill: #dcd938;
    --headline-yellow: #f5c617;
    --footer-text: #e2a92a;
    --body-text: #1d1d1d;
  }
  * { box-sizing: border-box; margin: 0; padding: 0; }
  html, body { width: 1200px; height: 1200px; overflow: hidden; }
  body {
    background: var(--stage);
    font-family: "Roboto Condensed", "Arial Narrow", sans-serif;
    position: relative;
  }
  .infographic {
    position: absolute;
    left: 150px; top: 20px;
    width: 900px; height: 1160px;
    background: var(--paper);
    display: flex; flex-direction: column;
  }
  .masthead { height: 428px; background: var(--ink); position: relative; }
  .masthead-title {
    position: absolute; left: 40px; top: 76px; width: 620px;
    text-align: center; line-height: 1;
  }
  .title-main { color: var(--paper); font-weight: 700; font-size: 68px; letter-spacing: 0.5px; }
  .title-sub { color: var(--paper); font-weight: 700; font-size: 58px; margin-top: -4px; }
  .title-abbr { color: var(--paper); font-weight: 700; font-size: 44px; margin-top: 6px; }
  .title-question { color: var(--headline-yellow); font-weight: 300; font-size: 56px; margin-top: 14px; }
  .title-process { color: var(--headline-yellow); font-weight: 300; font-size: 94px; margin-top: -2px; letter-spacing: 1px; }
  .masthead-sign { position: absolute; right: 38px; top: 130px; width: 280px; height: 300px; }
  .steps-band { height: 273px; display: block; }
  .steps-text {
    height: 139px; display: grid; grid-template-columns: repeat(3, 1fr);
    text-align: center; color: var(--body-text);
    font-weight: 300; font-size: 25px; line-height: 1.27;
    padding-top: 16px;
  }
  .steps-text p { padding: 0 34px; }
  .steps-text p:last-child { padding: 0 20px; }
  .flagman-row { height: 180px; position: relative; }
  .signal-art {
    position: absolute; left: 60px; top: 6px; width: 232px; height: 164px;
    background: linear-gradient(180deg, #f1f1f1, #dcdcdc);
    border-radius: 4px;
  }
  .flagman-callout {
    position: absolute; left: 292px; top: 0; width: 608px; height: 180px;
    background: var(--gold-box);
    clip-path: polygon(0 0, 100% 0, 100% 100%, 0 100%, 0 38px, 18px 26px, 0 14px);
    color: var(--ink); text-transform: uppercase;
    font-size: 27px; line-height: 1.3; padding: 16px 110px 0 39px;
  }
  .fine-print {
    height: 82px; padding: 10px 48px 0 46px;
    font-size: 15.5px; line-height: 1.38; color: var(--body-text);
  }
  .footer-bar {
    height: 59px; background: #181818;
    color: var(--footer-text); font-size: 14px;
    text-align: center; padding-top: 10px;
  }
</style>
</head>
<body>
  <article class="infographic">
    <header class="masthead">
      <div class="masthead-title">
        <div class="title-main">CROSSING RAILROAD</div>
        <div class="title-sub">RIGHT OF WAY</div>
        <div class="title-abbr">(ROW)</div>
        <div class="title-question">WHAT IS THE</div>
        <div class="title-process">PROCESS?</div>
      </div>
      <svg class="masthead-sign" viewBox="0 0 280 300" role="img" aria-label="Weathered yellow railroad crossing warning sign on a post">
        <defs>
          <linearGradient id="signTone" x1="0" y1="0" x2="1" y2="1">
            <stop offset="0" stop-color="#f7d62a"/>
            <stop offset="1" stop-color="#e0a414"/>
          </linearGradient>
        </defs>
        <rect x="130" y="250" width="18" height="50" fill="#bdbdbd"/>
        <polygon points="139,4 276,140 139,276 2,140" fill="url(#signTone)"/>
      </svg>
    </header>

    <svg class="steps-band" viewBox="0 0 900 273" width="900" height="273">
      <rect x="0" y="0" width="300" height="273" fill="var(--amber)"/>
      <rect x="300" y="0" width="300" height="273" fill="var(--gold)"/>
      <rect x="600" y="0" width="300" height="273" fill="var(--amber)"/>
      <polygon points="300,24 322,44 300,64" fill="var(--amber)"/>
      <polygon points="600,24 622,44 600,64" fill="var(--gold)"/>
      <line x1="300" y1="0" x2="300" y2="273" stroke="#fff" stroke-width="3"/>
      <line x1="600" y1="0" x2="600" y2="273" stroke="#fff" stroke-width="3"/>

      <polygon class="step-sign" points="150,28 258,136 150,244 42,136" fill="var(--sign-fill)" role="img" aria-label="Warning sign illustration showing an approaching train"/>
      <polygon class="step-sign" points="450,28 558,136 450,244 342,136" fill="var(--sign-fill)" role="img" aria-label="Warning sign illustration showing a crossing signal"/>
      <polygon class="step-sign" points="750,28 858,136 750,244 642,136" fill="var(--sign-fill)" role="img" aria-label="Warning sign illustration showing a road crossing railroad tracks"/>
    </svg>

    <section class="steps-text">
      <p>Contact Railroad to obtain application and specifications.</p>
      <p>Submit application to Railroad with engineering plans.</p>
      <p>When plans are approved, enter into license agreement with railroad</p>
    </section>

    <section class="flagman-row">
      <div class="signal-art" role="img" aria-label="Railroad crossing signal with crossbuck, red lights and lowered striped gate arm"></div>
      <div class="flagman-callout">With railroad safety protocols and approved work plan in place, coordinate with operations to obtain flagman</div>
    </section>

    <p class="fine-print">Railroads adhere to strict safety and notification standards so that both the entity creating an encumbrance on railroad property as well as the railroads themselves, establish clear rules to engagement that allow each to accomplish their own goals while minimizing risk to the public</p>

    <footer class="footer-bar">Every railroad company has a detailed process to ensure SAFETY and avoid interruption to operations when crossing railroad ROW</footer>
  </article>
</body>
</html>
```